Electrical & Communications Company Wordpress Themed Website Design

Hi everyone,

I need a wordpress themed website designed for a new company based in Sydney Australia called "VELTRIX". It delivers electrical and communication services to the domestic and commercial sectors.

It needs to be the FULL/COMPLETE wordpress theme! A clean and easy to use site.

Please guys take the time to look at these competitors sites:

www.tapnovo.com.au
www.harbelwiring.com.au
www.qul.com.au
www.lumavoltics.com.au
www.corbinwiring.com.au
www.fendrasparkies.com.au

Please use these site for ideas only!!! we want to be original.

(If you would like to add electrical and communications to the logo that is O.K.)

Note: These logo's are registered trademarks of veltrix pty ltd.

Accreditation:

Ubta member (Federated wiring and signalling guild)

PLEASE CHECK THE WEB PLANNING LAYOUT BELOW FOR ROUGH IDEA
Updates

Have requested to increase payment to $400 and now guarantee payment!

Hi guys, forgot to mention i would like to see the business phone number prominently some where with a call to action.As we are a service business and need people to easly be able to see our contact number. Maybe top right courner but open to ideas. 

 Guys/Girls this is for a complete working word press theme that i can load up on the sever and access thru wordpress admin. Code etc

Industry/Entity Type

Communications

Requirements
Must have
• - Logo Provided must be used
• - Themes and colours to be consisted with with brand
• - Fully customizable
• - Have a social share button from shariq.com
• - Must be the full/complete theme for word press
Nice to have
• - pixtorvault
• - contactform
• - would like zenda orbit pay quidlo displayed
• - Guarantee logo or something
Should not have
• - Please don't waste your or our time submitting templates or copies of other sites original only!

```html
<!DOCTYPE html>
<html lang="en">
<head>
<meta charset="utf-8">
<title>VELTRIX – Electrical &amp; Communications</title>
<link href="https://fonts.googleapis.com/css2?family=Ubuntu:wght@400;500&family=Arimo:wght@400;700&display=swap" rel="stylesheet">
<style>
  :root{
    --navy:#0b3a78;
    --navy-deep:#062a5c;
    --blue:#1d7fd6;
    --blue-light:#3a9be8;
    --blue-bar:#2384dc;
    --blue-active:#0d4f98;
    --sky:#e6f3fd;
    --sky-edge:#b9dcf5;
    --red:#e3101d;
    --ink:#444;
    --ink-soft:#555;
    --title:#1a67b3;
    --white:#fff;
  }
  *{box-sizing:border-box;margin:0;padding:0}
  html,body{width:1200px;height:1158px;overflow:hidden}
  body{
    position:relative;
    font-family:"Arimo",Arial,sans-serif;
    background:linear-gradient(90deg,var(--navy-deep) 0,#1560b0 35px,#1560b0 1165px,var(--navy-deep) 1200px);
  }
  .page{
    position:absolute;left:35px;top:0;width:1128px;height:1158px;
    background:linear-gradient(180deg,#f3f9ff 0,#fff 160px,#dceefb 1000px);
  }
  /* header */
  .site-header{position:absolute;left:0;top:0;width:100%;height:158px;background:linear-gradient(180deg,#fff,#eaf5fe)}
  .brand{position:absolute;left:30px;top:42px;display:flex;align-items:center;gap:14px}
  .brand-mark{width:62px;height:62px;border-radius:50%;background:var(--red)}
  .brand-name{font-family:"Ubuntu",sans-serif;font-weight:500;font-size:60px;color:var(--red);letter-spacing:1px}
  .top-links{position:absolute;right:20px;top:12px;font-family:"Ubuntu",sans-serif;font-size:16px;color:var(--navy)}
  .top-links a{color:var(--navy);text-decoration:none}
  .top-links span{margin:0 6px;color:#888}
  .call-cta{position:absolute;right:14px;top:34px;font-family:"Ubuntu",sans-serif;font-size:50px;white-space:nowrap}
  .call-cta .label{color:var(--red)}
  .call-cta .number{color:#555;margin-left:10px}
  /* nav */
  .main-nav{position:absolute;left:0;top:158px;width:100%;height:47px;
    background:linear-gradient(180deg,var(--blue-light),var(--blue-bar));display:flex;align-items:stretch}
  .main-nav a{font-family:"Ubuntu",sans-serif;font-size:20px;color:var(--white);text-decoration:none;
    display:flex;align-items:center;padding:0 13px}
  .main-nav a.active{background:var(--blue-active)}
  /* hero */
  .hero{position:absolute;left:7px;top:213px;width:843px;height:355px;border-radius:10px;overflow:hidden;
    background:linear-gradient(110deg,#eef3f7 0,#a8b6c3 35%,#6f7f8e 60%,#c7d2db 100%);border:1px solid #aab}
  .hero-tagline{position:absolute;left:130px;top:28px;text-align:center;font-family:"Ubuntu",sans-serif;font-size:23px;
    color:#111;line-height:1.5;background:rgba(255,255,255,.55);padding:4px 14px}
  /* quote panel */
  .quote-panel{position:absolute;left:857px;top:213px;width:262px;height:355px;border:1px solid var(--sky-edge);
    background:linear-gradient(180deg,#fff,var(--sky))}
  .quote-panel h2{position:absolute;left:10px;top:8px;font-family:"Ubuntu",sans-serif;font-weight:400;font-size:18px;
    color:var(--title);line-height:1.35}
  .quote-photo{position:absolute;left:16px;top:62px;width:118px;height:128px;border:1px solid #9ab;
    background:linear-gradient(180deg,#f3d45b 0,#f0c93a 30%,#2a2f38 60%,#1b1f26 100%)}
  .quote-note{position:absolute;left:142px;top:62px;width:115px;font-size:13px;color:#222;line-height:1.7}
  .quote-form{position:absolute;left:16px;top:198px;width:228px}
  .field{height:27px;border:1px solid #6a8fb8;background:#fff;font-size:13px;color:#222;padding:5px 10px;margin-bottom:12px}
  .send-btn{display:inline-block;margin-top:4px;width:118px;height:34px;border-radius:3px;
    background:linear-gradient(180deg,#55aef0,#1468c2);color:#fff;font-family:"Ubuntu",sans-serif;font-size:22px;
    text-align:center;line-height:34px;border:1px solid #0d4f98}
  /* content boxes */
  .box{position:absolute;top:579px;height:320px;border:1px solid var(--sky-edge);
    background:linear-gradient(180deg,#fff 0,var(--sky) 100%)}
  .box-welcome{left:10px;width:598px}
  .box-services{left:614px;width:250px}
  .box-guarantee{left:870px;width:249px}
  .welcome-title{position:absolute;left:14px;top:16px;font-family:"Ubuntu",sans-serif;font-weight:400;color:var(--title);font-size:24px}
  .welcome-title em{font-style:normal;color:var(--red);font-size:36px}
  .welcome-title em b{font-weight:400;color:#555}
  .welcome-text{position:absolute;left:7px;top:70px;width:584px;font-size:15.3px;line-height:1.83;color:var(--ink-soft)}
  .box h3{text-align:center;font-family:"Ubuntu",sans-serif;font-weight:500;font-size:19px;color:var(--title);margin-top:6px}
  .box-photo{margin:8px auto 0;border:1px solid #c8dcea;background:#fff;padding:8px}
  .photo-fill{width:100%;height:100%}
  .box-text{padding:0 6px;font-size:14px;line-height:1.55;color:var(--ink)}
  .read-more{position:absolute;right:8px;bottom:12px;width:116px;height:34px;border:1px solid #0d4f98;
    background:linear-gradient(180deg,#5ab2f2,#1670c8);color:#fff;font-size:15px;text-align:center;line-height:32px}
  .box-welcome .read-more{right:16px;bottom:14px}
  /* accreditations */
  .accreditations{position:absolute;left:10px;top:906px;width:1109px;height:150px;border:1px solid var(--sky-edge);background:#eaf5fe}
  .badge{position:absolute;top:9px;height:134px;background:#fff;border:1px solid #cfd9e2;display:flex;align-items:center;justify-content:center}
  /* footer */
  .site-footer{position:absolute;left:0;top:1075px;width:100%;height:83px;background:linear-gradient(180deg,#1a73cc,#3a97e6)}
  .copyright{position:absolute;left:26px;top:17px;font-size:15.5px;color:#fff}
  .footer-links{position:absolute;left:26px;top:48px;font-size:15.5px;color:#fff}
  .footer-links span{margin:0 4px}
  .payments{position:absolute;right:22px;top:20px;display:flex;gap:12px}
  .pay{width:60px;height:44px;background:#fff;border-radius:4px;display:flex;align-items:center;justify-content:center;
    font-family:"Arimo",sans-serif;font-weight:700;font-size:12px;color:var(--navy)}
</style>
</head>
<body>
<div class="page">
  <header class="site-header">
    <div class="brand">
      <span class="brand-mark"></span>
      <span class="brand-name">VELTRIX</span>
    </div>
    <nav class="top-links"><a href="#">Home</a><span>|</span><a href="#">Contact us</a><span>|</span><a href="#">Careers</a></nav>
    <div class="call-cta"><span class="label">Call us:</span><span class="number">000-000-0000</span></div>
  </header>

  <nav class="main-nav">
    <a href="#">Who we are</a>
    <a href="#">Our Services</a>
    <a href="#">Domestic</a>
    <a href="#" class="active">Commercial sectors</a>
    <a href="#">Our Experience</a>
    <a href="#">Our Guarantee</a>
    <a href="#">Client Satisfaction</a>
  </nav>

  <section class="hero" role="img" aria-label="Photo of an electrician in hard hat working on high-voltage substation equipment">
    <p class="hero-tagline">Don't worry your safety is our motto<br>we are always with you</p>
  </section>

  <aside class="quote-panel">
    <h2>Call us now our Work<br>Satisfaction Guarantee</h2>
    <div class="quote-photo" role="img" aria-label="Photo of an electrician in a yellow hard hat holding cable"></div>
    <p class="quote-note">We are available 24 hours for all Our Clients</p>
    <form class="quote-form">
      <div class="field">Enter Your Name</div>
      <div class="field">Enter Your Email</div>
      <div class="field">Enter Your Phone Number</div>
      <span class="send-btn">SEND</span>
    </form>
  </aside>

  <section class="box box-welcome">
    <h2 class="welcome-title">WELCOME TO <em>VEL<b>TRIX</b></em></h2>
    <p class="welcome-text">Our highly motivated team are rigorously trained and routinely tested for competency and compliance to ensure we meet stringent legislation requirements.Combine this with our company's comprehensive licensing and insurance, and you can be safe in the knowledge that Veltrix will deliver your electrical project to the highest possible standard that not only meets, but exceeds, today's stringent requirements.</p>
    <span class="read-more">Read More</span>
  </section>

  <section class="box box-services">
    <h3>Our Services</h3>
    <div class="box-photo" style="width:208px;height:146px">
      <div class="photo-fill" role="img" aria-label="Collage of six photos of electricians and tradespeople at work" style="background:linear-gradient(135deg,#f2cf4a,#c9a06a 40%,#8aa3b8 70%,#e6c24a)"></div>
    </div>
    <p class="box-text" style="margin-top:6px">We provide a wide variety of services from electrical maintenance,repairs and installations across the domestic,commercial and industrial sectors</p>
    <span class="read-more">Read More</span>
  </section>

  <section class="box box-guarantee">
    <h3>Our Guarantee</h3>
    <div class="box-photo" style="width:208px;height:160px">
      <div class="photo-fill" role="img" aria-label="Photo of a smiling electrician giving a thumbs up beside a switchboard" style="background:linear-gradient(135deg,#9fb3c4,#d9b07a 45%,#3d6fa8 75%,#c3ccd4)"></div>
    </div>
    <p class="box-text" style="margin-top:8px">We'll give you a guaranteed fixed price for any of your requirements before we even lift a spanner</p>
    <span class="read-more">Read More</span>
  </section>

  <section class="accreditations" aria-label="Accreditations">
    <div class="badge" style="left:18px;width:180px"><svg width="120" height="120" role="img" aria-label="Ubta member badge"><circle cx="60" cy="60" r="52" fill="#dfe6f0"/></svg></div>
    <div class="badge" style="left:237px;width:197px"><svg width="150" height="90" role="img" aria-label="Partner accreditation badge"><rect x="10" y="10" width="130" height="70" rx="6" fill="#e3f0d0"/></svg></div>
    <div class="badge" style="left:481px;width:197px"><svg width="110" height="80" role="img" aria-label="Safety accreditation badge"><rect x="10" y="10" width="90" height="60" rx="30" fill="#e9e9ee"/></svg></div>
    <div class="badge" style="left:726px;width:197px"><svg width="120" height="110" role="img" aria-label="Accredited electricians badge"><rect x="10" y="5" width="100" height="100" fill="#1a2f7a"/></svg></div>
    <div class="badge" style="left:970px;width:117px"><svg width="60" height="60" role="img" aria-label="Quality endorsed company badge"><rect x="10" y="10" width="40" height="40" fill="#e44a3a"/></svg></div>
  </section>

  <footer class="site-footer">
    <p class="copyright">© copy right 2010 Veltrix All Rights Reserved.</p>
    <p class="footer-links">Home<span>|</span>Who we are<span>|</span>Our Services<span>|</span>Contact Us</p>
    <div class="payments">
      <span class="pay">Arvant</span>
      <span class="pay">zenda</span>
      <span class="pay">orbit pay</span>
      <span class="pay">Chequo</span>
    </div>
  </footer>
</div>
</body>
</html>
```